Electrical needs letterhead design

Need a letterhead design for an electrical company. Using the same colours as to what are used in the logo.
After a modern design.

Want the logo in top right or top left.

Must include...

ABN 71 804 239 356
PHONE 0458203917
www.kelmaroo.com.au
jed@kelmaroo.com.au

'ABN' and 'PHONE' in bold.

Keep it basic. Logo top left, details either next to it or far right corner. Dont want any other objects included.

Electrical

```html
<!DOCTYPE html>
<html lang="en">
<head>
<meta charset="utf-8">
<title>Kelmaroo — Letterhead</title>
<link rel="stylesheet" href="https://fonts.googleapis.com/css2?family=PT+Sans:wght@400;700&family=Roboto+Condensed:wght@400;700&family=Great+Vibes&display=swap">
<style>
  :root {
    --brand: #a8322d;
    --ink: #111111;
    --paper: #ffffff;
  }
  * { margin: 0; padding: 0; box-sizing: border-box; }
  html, body { width: 848px; height: 1200px; overflow: hidden; background: var(--paper); }
  .letterhead {
    position: relative;
    width: 848px;
    height: 1200px;
    overflow: hidden;
    background: var(--paper);
    font-family: "PT Sans", "Helvetica Neue", Arial, sans-serif;
    color: var(--ink);
  }
  .company {
    position: absolute; left: 30px; top: 70px;
    display: flex; align-items: center; gap: 14px;
  }
  .company-dot {
    width: 26px; height: 26px; border-radius: 50%;
    background: var(--brand);
  }
  .company-name {
    font-family: "PT Sans", Arial, sans-serif;
    font-weight: 400;
    font-size: 48px;
    line-height: 1;
    color: var(--brand);
  }
  .salutation {
    position: absolute; left: 50px; top: 242px;
    font-weight: 700; font-size: 21px; line-height: 28px;
  }
  .body-copy {
    position: absolute; left: 50px; width: 790px;
    font-size: 17.6px; line-height: 23px; white-space: nowrap;
  }
  .p1 { top: 286px; }
  .p2 { top: 394px; }
  .p3 { top: 484px; }
  .p4 { top: 620px; }
  .p5 { top: 669px; }
  .signature { position: absolute; left: 476px; top: 866px; }
  .signature-name {
    font-family: "Great Vibes", cursive;
    font-size: 62px; line-height: 1; color: var(--ink);
  }
  .signature-role {
    position: absolute; left: 148px; top: 66px;
    font-size: 23px; white-space: nowrap;
  }
  .contact-bar {
    position: absolute; left: 0; top: 1160px; width: 848px;
    font-family: "Roboto Condensed", "Arial Narrow", sans-serif;
    font-size: 16px;
  }
  .contact-item { position: absolute; white-space: nowrap; }
  .contact-item b { font-weight: 700; color: var(--ink); }
  .contact-item span { color: var(--brand); }
  .abn { left: 54px; }
  .phone { left: 210px; }
  .email { left: 370px; }
  .web { left: 607px; }
</style>
</head>
<body>
<main class="letterhead">
  <header class="company">
    <span class="company-dot"></span>
    <span class="company-name">Kelmaroo</span>
  </header>

  <h1 class="salutation">Lorem ipsum dolor,</h1>

  <p class="body-copy p1">Lorem ipsum dolor sit amet, consectetur adipisicing elit, sed do eiusmod tempor incididunt ut<br>magna aliqua. Ut enim ad minim veniam, quis nostrud exercitation ullamco laboris nisi ut aliqu.</p>
  <p class="body-copy p2">Lorem ipsum dolor sit amet, consectetur adipisicing elit, sed do eiusmod tempor incididunt<br>magna aliqua. Ut enim ad minim veniam, quis nostrud exercitation.</p>
  <p class="body-copy p3">Lorem ipsum dolor sit amet, consectetur adipisicing elit, sed do eiusmod tempor incididunt<br>magna aliqua. Ut enim ad minim veniam, quis nostrud exercitation ullamco laboris nisi ut al<br>do consequa.Lorem ipsum dolor sit amet, consectetur adipisicing elit, sed do eiusmod temp<br>bore et dolore magna aliqua. Ut enim ad minim veniam, quis.</p>
  <p class="body-copy p4">Lorem ipsum dolor sit amet, consectetur adipisicing elit, sed do eiusmod tempor incididunt.</p>
  <p class="body-copy p5">Lorem ipsum dolor sit amet, consectetur adipisicing elit, sed do eiusmod tempor incididunt<br>magna aliqua. Ut enim ad minim veniam, quis nostrud exercitation ullamco laboris nisi ut al<br>do consequa.Lorem ipsum dolor sit amet, consectetur adipisicing elit, sed do eiusmod temp<br>bore et dolore magna aliqua. Ut enim ad minim veniam, quis.</p>

  <div class="signature">
    <div class="signature-name">Your Name</div>
    <div class="signature-role">Director</div>
  </div>

  <footer class="contact-bar">
    <div class="contact-item abn"><b>ABN:</b> <span>71 804 239 356</span></div>
    <div class="contact-item phone"><b>PHONE:</b> <span>0458203917</span></div>
    <div class="contact-item email"><b>Email:</b> <span>jed@kelmaroo.com.au</span></div>
    <div class="contact-item web"><b>Web:</b> <span>www.kelmaroo.com.au</span></div>
  </footer>
</main>
</body>
</html>
```